Unique Builder wordpress website - Supply Graphics Only

We need a brand new website for a building company in Perth, Australia who constructs insulated panels (sip).
What is a SIP?
A SIP is a high-performance building panel used for floors, walls, and roofs in residential and commercial buildings. Panels are typically made using Expanded Polystyrene (EPS) sandwiched between two structural skins.
The design must incorporate a slick professional look and keep to the logo colours (Lime green & Blacks). The logo must not change colours or be altered. (
We will convert the graphics to a wordpress site. We have our own coders)
Design:
The website design must be clean, mobile friendly and the final design will be adapted to WordPress CMS.
The menus must contain dropdown menus and front page may contain a youtube video at a later date.
Fonts must be clear and easy to read
The contact us page will need to have an online form and google map.
The 16 pages listed will be the complete site and are for reference only. For this project the winning designer would need to supply the Homepage, and 1 inner pages only as PSD files.
The structure is as follows:
Home
About us
High Tech Homes
What is a sip
Benefits
FAQ
Designs
Residential
Granny Flats
Architectural design
Photo Gallery <--- Would be great if a sample design can be provided
Services
Project management and custom design
Site Assembly
Kit Supply
Contact us
***We don't need the designer to design every page however a 1 inner page would be ideal****
Our Competitors websites
Note: the following websites look crap however, the following websites are some of our competitors. We want a clean and awesome layout.
http://www.vorkalite.com.au/
http://trenmoreworks.com.au/
http://www.bralvexa.net.au/
New home builders and commercial builders
Building
5+ page

```html
<!DOCTYPE html>
<html lang="en">
<head>
<meta charset="utf-8">
<title>VantraBuild – Advanced Building Technology</title>
<link href="https://fonts.googleapis.com/css2?family=Exo+2:wght@400;500;600&family=PT+Sans:wght@400;700&display=swap" rel="stylesheet">
<style>
:root{
  --lime:#8dc63f;
  --lime-dark:#6f9e23;
  --lime-light:#a9d251;
  --ink:#1f1f1f;
  --nav:#262626;
  --subnav:#3a3a3a;
  --band:#333333;
  --footer:#222222;
  --text:#555555;
  --white:#ffffff;
}
*{margin:0;padding:0;box-sizing:border-box}
html,body{width:946px;height:1200px;overflow:hidden;background:var(--white)}
body{position:relative;font-family:"PT Sans",Arial,sans-serif;color:var(--text)}
.abs{position:absolute}

/* Header */
.site-header{left:0;top:0;width:946px;height:89px;background:var(--white)}
.brand{left:87px;top:30px;display:flex;align-items:center;gap:10px}
.brand-mark{width:26px;height:26px;background:var(--ink);border-radius:50%}
.brand-name{font-family:"Exo 2",sans-serif;font-weight:500;font-size:26px;color:var(--ink);line-height:1}
.brand-tag{left:123px;top:57px;font-family:"Exo 2",sans-serif;font-size:7px;font-weight:500;color:var(--ink);letter-spacing:.2px;text-transform:uppercase}
.call{left:702px;top:43px;display:flex;align-items:center;gap:6px}
.call-label{font-size:8px;color:#666;line-height:1}
.call-number{font-family:"Exo 2",sans-serif;font-size:16px;color:#444;line-height:1.15}

/* Main nav */
.main-nav{left:0;top:89px;width:946px;height:50px;background:linear-gradient(#2d2d2d,#1c1c1c)}
.main-nav a{position:absolute;top:0;height:50px;line-height:47px;transform:translateX(-50%);font-family:"Exo 2",sans-serif;font-size:9.5px;font-weight:500;color:var(--white);text-decoration:none;text-transform:uppercase;white-space:nowrap}
.main-nav .active{left:125px;width:73px;text-align:center;color:var(--ink);font-weight:600;background:linear-gradient(var(--lime-light),var(--lime-dark));height:44px;top:0}
.tab-point{left:88px;top:133px}

/* Sub nav */
.sub-nav{left:0;top:139px;width:946px;height:43px;background:var(--subnav);display:flex;align-items:center;justify-content:center;gap:12px;padding-left:4px}
.sub-nav a{font-family:"Exo 2",sans-serif;font-size:9px;color:var(--white);text-decoration:none;text-transform:uppercase;white-space:nowrap}
.sub-nav .dot{width:5px;height:5px;border-radius:50%;background:#5a5a5a}

/* Hero */
.hero{left:0;top:182px;width:946px;height:396px;background:linear-gradient(100deg,#86b83a,#9bc84a 50%,#84b538)}
.slider{left:87px;top:200px;width:771px;height:362px;background:#2c2c2c;padding:5px}
.slide-photo{width:100%;height:100%;background:linear-gradient(#c9cdd0 0%,#b7bcb5 28%,#8f8a5a 35%,#7c7a4a 60%,#a7895f 70%,#807c4c 80%,#6c6a42 100%)}
.slide-caption{left:93px;top:485px;width:760px;height:72px;background:rgba(30,30,30,.78)}
.slide-title{left:122px;top:508px;font-family:"Exo 2",sans-serif;font-size:23px;color:var(--white);letter-spacing:.3px}
.slide-arrows{left:777px;top:511px}

/* Welcome */
.welcome-title{left:87px;top:606px;font-family:"Exo 2",sans-serif;font-size:17px;font-weight:500;color:var(--ink)}
.intro{left:87px;top:641px;width:600px;font-size:9px;line-height:20px;color:#666}
.benefits{left:117px;top:697px;list-style:none}
.benefits li{display:flex;align-items:center;gap:3px;height:29.7px;font-size:10px;color:#444}
.video{left:615px;top:689px;width:243px;height:150px;border:3px solid var(--ink);background:linear-gradient(90deg,#b9b2a0,#dcdcdc 45%,#e9e9e9 70%,#c7c3b8)}
.play{left:713px;top:740px}

/* Call band */
.cta-band{left:0;top:878px;width:946px;height:190px;background:var(--band)}
.cta-title{left:140px;top:907px;width:666px;text-align:center;font-size:16px;line-height:20px;color:var(--white)}
.cta-text{left:100px;top:959px;width:746px;text-align:center;font-size:9px;color:var(--white)}
.cta-button{left:406px;top:994px;width:135px;height:44px;background:linear-gradient(var(--lime-light),var(--lime-dark));border-radius:2px;text-align:center;line-height:44px;font-family:"Exo 2",sans-serif;font-size:11.5px;font-weight:600;color:#2a2a2a;text-decoration:none}

/* Footer */
.contact-bar{left:0;top:1068px;width:946px;height:66px;background:linear-gradient(#262626,#1b1b1b);border-top:1px solid #444}
.contact-item{top:1095px;display:flex;align-items:center;gap:6px;font-size:9px;color:#ddd;white-space:nowrap}
.social{top:1090px;width:22px;height:22px;border-radius:50%}
.bottom-bar{left:0;top:1134px;width:946px;height:66px;background:var(--band);border-top:1px solid #3f3f3f}
.legal{left:87px;top:1162px;font-size:9px;color:#ccc}
.legal a{color:#ccc;text-decoration:none}
.copyright{right:88px;top:1162px;font-size:9px;color:#ccc}
</style>
</head>
<body>

<header class="site-header abs">
  <div class="brand abs">
    <span class="brand-mark"></span>
    <span class="brand-name">VantraBuild</span>
  </div>
  <div class="brand-tag abs">Advanced Building Technology</div>
  <div class="call abs">
    <svg width="32" height="32" viewBox="0 0 32 32" aria-hidden="true">
      <circle cx="16" cy="16" r="14" fill="none" stroke="var(--lime)" stroke-width="2.5"/>
      <path d="M11 9l3 0 1 4-2 1.5c1 2 2.5 3.5 4.5 4.5L19 17l4 1 0 3c-6 1-13-6-12-12z" fill="var(--lime)"/>
    </svg>
    <div>
      <div class="call-label">If Any Questions? Call Now</div>
      <div class="call-number">123 456 789 000</div>
    </div>
  </div>
</header>

<nav class="main-nav abs">
  <a class="active" href="#">Home</a>
  <a href="#" style="left:212px">About Us</a>
  <a href="#" style="left:317px">What is a SIP</a>
  <a href="#" style="left:420px">Benefits</a>
  <a href="#" style="left:502px">FAQ</a>
  <a href="#" style="left:599px">Photo Gallery</a>
  <a href="#" style="left:707px">Services</a>
  <a href="#" style="left:807px">Contact Us</a>
</nav>
<svg class="tab-point abs" width="73" height="9" viewBox="0 0 73 9" aria-hidden="true">
  <polygon points="0,0 73,0 36.5,9" fill="var(--lime-dark)"/>
</svg>

<nav class="sub-nav abs">
  <a href="#">High Tech Homes</a><span class="dot"></span>
  <a href="#">Residential</a><span class="dot"></span>
  <a href="#">Granny Flats Site</a><span class="dot"></span>
  <a href="#">Assembly</a><span class="dot"></span>
  <a href="#">Kit Supply</a><span class="dot"></span>
  <a href="#">Architectural Design</a><span class="dot"></span>
  <a href="#">Project Management and Custom Design</a>
</nav>

<section class="hero abs"></section>
<div class="slider abs">
  <div class="slide-photo" role="img" aria-label="Timber-framed insulated wall panels standing on a building site with trees behind"></div>
</div>
<div class="slide-caption abs"></div>
<div class="slide-title abs">PROJECT MANAGEMENT AND CUSTOM DESIGN</div>
<svg class="slide-arrows abs" width="56" height="24" viewBox="0 0 56 24" aria-hidden="true">
  <circle cx="12" cy="12" r="11" fill="#bbb" stroke="#777"/>
  <polygon points="8,12 14,7 14,17" fill="#fff"/>
  <circle cx="43" cy="12" r="11" fill="#bbb" stroke="#777"/>
  <polygon points="47,12 41,7 41,17" fill="#fff"/>
</svg>

<h1 class="welcome-title abs">WELCOME TO VANTRA BUILD</h1>
<div class="intro abs">
  <p>Vantrabuild are designers and manufacturers of an engineered structural insulated panel and concealed structural frame building product.</p>
  <p>sips is rapidly becoming the building method of choice because of its overwhelming benefits and proven suitability.</p>
</div>
<ul class="benefits abs">
  <li><svg width="11" height="11" viewBox="0 0 11 11" aria-hidden="true"><circle cx="5.5" cy="5.5" r="5.5" fill="var(--lime)"/><path d="M3 5.6l1.8 1.8L8.2 4" fill="none" stroke="#fff" stroke-width="1.4"/></svg>High level of captive insulation. (warm in winter cool in summer)</li>
  <li><svg width="11" height="11" viewBox="0 0 11 11" aria-hidden="true"><circle cx="5.5" cy="5.5" r="5.5" fill="var(--lime)"/><path d="M3 5.6l1.8 1.8L8.2 4" fill="none" stroke="#fff" stroke-width="1.4"/></svg>Very strong, light weight and durable.</li>
  <li><svg width="11" height="11" viewBox="0 0 11 11" aria-hidden="true"><circle cx="5.5" cy="5.5" r="5.5" fill="var(--lime)"/><path d="M3 5.6l1.8 1.8L8.2 4" fill="none" stroke="#fff" stroke-width="1.4"/></svg>20 + year history of performance in cyclonic locations in WA</li>
  <li><svg width="11" height="11" viewBox="0 0 11 11" aria-hidden="true"><circle cx="5.5" cy="5.5" r="5.5" fill="var(--lime)"/><path d="M3 5.6l1.8 1.8L8.2 4" fill="none" stroke="#fff" stroke-width="1.4"/></svg>Reduced build time (save time save money it's that easy)</li>
  <li><svg width="11" height="11" viewBox="0 0 11 11" aria-hidden="true"><circle cx="5.5" cy="5.5" r="5.5" fill="var(--lime)"/><path d="M3 5.6l1.8 1.8L8.2 4" fill="none" stroke="#fff" stroke-width="1.4"/></svg>Energy efficient ( less energy to build and less energy to run ie lower power bills)</li>
</ul>
<div class="video abs" role="img" aria-label="Video still of a timber ladder against white panel walls under construction"></div>
<svg class="play abs" width="48" height="48" viewBox="0 0 48 48" aria-hidden="true">
  <circle cx="24" cy="24" r="22" fill="rgba(120,120,120,.55)" stroke="#ddd" stroke-width="2"/>
  <polygon points="18,13 35,24 18,35" fill="#fff"/>
</svg>

<section class="cta-band abs"></section>
<p class="cta-title abs">Vantrabuild panels can be used in residential and commercial building and are fully compliant to Australian standards.</p>
<p class="cta-text abs">We specialize in supplying on time and on budget, with high quality structural kits to builders and developers specific to their needs or requirements.</p>
<a class="cta-button abs" href="#">CONTACT NOW</a>

<footer>
  <div class="contact-bar abs"></div>
  <div class="contact-item abs" style="left:87px">
    <svg width="8" height="12" viewBox="0 0 8 12" aria-hidden="true"><path d="M4 0a4 4 0 0 1 4 4c0 3-4 8-4 8S0 7 0 4a4 4 0 0 1 4-4z" fill="var(--lime)"/><circle cx="4" cy="4" r="1.5" fill="#222"/></svg>
    Level 6, Lorem Ipsm, Lorem Ipsm - 123 456
  </div>
  <div class="contact-item abs" style="left:298px">
    <svg width="11" height="11" viewBox="0 0 11 11" aria-hidden="true"><rect width="11" height="11" rx="2" fill="var(--lime)"/><path d="M3 2.5h1.5l.5 2-1 .7c.5 1 1.2 1.7 2.2 2.2l.7-1 2 .5V8.5C6 9 2.5 5.5 3 2.5z" fill="#222"/></svg>
    123 456 789 00
  </div>
  <div class="contact-item abs" style="left:404px">
    <svg width="12" height="12" viewBox="0 0 12 12" aria-hidden="true"><rect x="0" y="3" width="12" height="9" rx="1" fill="var(--lime)"/><rect x="3" y="0" width="6" height="4" fill="var(--lime)"/><rect x="2.5" y="6" width="7" height="1" fill="#222"/><rect x="2.5" y="8.5" width="7" height="1" fill="#222"/></svg>
    123 456 789 00
  </div>
  <div class="contact-item abs" style="left:512px">
    <svg width="13" height="9" viewBox="0 0 13 9" aria-hidden="true"><rect width="13" height="9" fill="var(--lime)"/><path d="M0 0l6.5 5L13 0" fill="none" stroke="#222" stroke-width="1"/></svg>
    info@domainname.com
  </div>
  <span class="social abs" style="left:755px;background:#3b5998" aria-label="Social profile"></span>
  <span class="social abs" style="left:782px;background:#4ab3e6" aria-label="Social profile"></span>
  <span class="social abs" style="left:809px;background:#1d86b8" aria-label="Social profile"></span>
  <span class="social abs" style="left:836px;background:#f26b1d" aria-label="News feed"></span>

  <div class="bottom-bar abs"></div>
  <div class="legal abs"><a href="#">Privacy Policy</a> &nbsp;|&nbsp; <a href="#">Sitemap</a></div>
  <div class="copyright abs">Copyrights@2016 Vantra Build. All Rights Reserved.</div>
</footer>

</body>
</html>
```